Logo + Business Card design for a new start-up

For a new start-up company, a global brand expansion agency (marketing, brand consulting solutions) we're looking for a creative designer to help us design both the company logo and business card for project managers.

The name of the company is 'Harrowgate Market Partners' (abbreviated: HMP, website: harrowgatemarketpartners.example)

The logo design should give the company an image of "corporate" (serious), but not too plain/simple. Playing with overlapping fonts, or font colors is an option. Logo with only the abbreviation HMP is also an option.

The business cards need to have a touch of creativity to them, any style/colors can be used, and should underline the nature of business.

```html
<!DOCTYPE html>
<html lang="en">
<head>
<meta charset="utf-8">
<title>Harrowgate Market Partners – Business Card</title>
<link rel="stylesheet" href="https://fonts.googleapis.com/css2?family=Arimo:wght@400&display=swap">
<style>
  :root {
    --paper: #ffffff;
    --ink: #000000;
    --band: #000000;
    --on-band: #ffffff;
    --mint: #72fecf;
    --lime: #a6f55a;
  }
  html, body {
    margin: 0;
    padding: 0;
    width: 1200px;
    height: 700px;
    overflow: hidden;
    background: var(--paper);
  }
  .card {
    position: relative;
    width: 1200px;
    height: 700px;
    overflow: hidden;
    background: var(--paper);
    font-family: "Arimo", Arial, sans-serif;
    font-weight: 400;
    color: var(--ink);
  }
  .card p { margin: 0; line-height: 1; white-space: nowrap; }

  /* Colour bands */
  .band-dark   { position: absolute; left: 0; top: 240px; width: 1200px; height: 351px; background: var(--band); }
  .band-lime   { position: absolute; left: 0; top: 591px; width: 1200px; height: 15px;  background: var(--lime); }
  .band-mint   { position: absolute; left: 0; top: 606px; width: 1200px; height: 94px;  background: var(--mint); }

  /* Brand name */
  .brand { position: absolute; left: 76px; top: 108px; color: var(--ink); }
  .brand-name-main { font-size: 84px; letter-spacing: -1px; }
  .brand-name-sub  { font-size: 38px; margin-top: 8px; }

  /* Tag lines */
  .tagline { position: absolute; left: 790px; font-size: 33px; color: var(--ink); }
  .tagline-one { top: 143px; }
  .tagline-two { top: 203px; }

  /* Contact list */
  .contact-icon { position: absolute; }
  .icon-phone { left: 82px;  top: 323px; width: 58px; height: 62px; }
  .icon-web   { left: 80px;  top: 416px; width: 63px; height: 63px; }
  .icon-home  { left: 78px;  top: 503px; width: 71px; height: 66px; }

  .contact-text { position: absolute; color: var(--on-band); font-size: 29px; }
  .contact-phone   { left: 181px; top: 322px; }
  .contact-phone p + p { margin-top: 8px; }
  .contact-web     { left: 182px; top: 434px; }
  .contact-address { left: 186px; top: 507px; }
  .contact-address p + p { margin-top: 8px; }

  /* Person */
  .person { position: absolute; left: 705px; top: 400px; width: 400px; text-align: center; color: var(--on-band); }
  .person-name  { font-size: 53px; }
  .person-title { font-size: 38px; margin-top: 6px; }
</style>
</head>
<body>
<div class="card">
  <div class="band-dark"></div>
  <div class="band-lime"></div>
  <div class="band-mint"></div>

  <div class="brand">
    <p class="brand-name-main">HARROWGATE</p>
    <p class="brand-name-sub">Market Partners</p>
  </div>

  <p class="tagline tagline-one">Tag line 1 here</p>
  <p class="tagline tagline-two">Tag line 2 here</p>

  <svg class="contact-icon icon-phone" viewBox="0 0 58 62" aria-label="Phone">
    <rect x="0" y="0" width="58" height="62" rx="8" fill="var(--mint)"/>
    <path d="M22 10 L28 22 L24 26 Q28 36 34 42 L38 38 L48 46 L43 53 Q32 54 23 42 Q14 30 16 14 Z" fill="none" stroke="#000" stroke-width="3" stroke-linejoin="round"/>
  </svg>
  <div class="contact-text contact-phone">
    <p>+ 000-000-0000</p>
    <p>+ 000-000-0000</p>
  </div>

  <svg class="contact-icon icon-web" viewBox="0 0 63 63" aria-label="Website">
    <g fill="none" stroke="var(--mint)" stroke-width="3">
      <circle cx="31.5" cy="31.5" r="29.5"/>
      <ellipse cx="31.5" cy="31.5" rx="13" ry="29.5"/>
      <line x1="31.5" y1="2" x2="31.5" y2="61"/>
      <line x1="2" y1="31.5" x2="61" y2="31.5"/>
      <line x1="7" y1="16" x2="56" y2="16"/>
      <line x1="7" y1="47" x2="56" y2="47"/>
    </g>
  </svg>
  <div class="contact-text contact-web">
    <p>harrowgatemarketpartners.example</p>
  </div>

  <svg class="contact-icon icon-home" viewBox="0 0 71 66" aria-label="Address">
    <g fill="none" stroke="var(--mint)" stroke-width="3">
      <polyline points="2,24 35.5,2 69,24"/>
      <line x1="2" y1="24" x2="69" y2="24"/>
      <rect x="12" y="30" width="47" height="34"/>
      <rect x="29" y="44" width="13" height="20"/>
      <polyline points="44,7 44,2 50,2 50,11"/>
    </g>
    <rect x="17" y="37" width="8" height="8" fill="var(--mint)"/>
    <rect x="46" y="37" width="8" height="8" fill="var(--mint)"/>
  </svg>
  <div class="contact-text contact-address">
    <p>555 Somewhere St, Suite 100</p>
    <p>Somewhere City, XX 00000</p>
  </div>

  <div class="person">
    <p class="person-name">John Doe</p>
    <p class="person-title">Title Here</p>
  </div>
</div>
</body>
</html>
```